Flyer for the Harvest of lanterns conference

Flyer design for an annual international conference called "MERIVAL 2017". This is a conference for young adults, so we hope to produce a design that is both professional and appealing to young people in general

We'd like the flyer to showcase the conference brand logo, and clearly highlight the key information to people who will read it.

Target Market(s)

Young people, young adults

Industry/Entity Type

Religious

Font styles to use
Sans Serif

Colors

Designer to choose colors to be used in the design.

Requirements
Must have
• - Should be only one page (Vertical or Horizontal).
• - the MERVAL logo and all the information found in the attached text file. This includes: Main topic: Your sons and daughters shall prophesy,
• Dates and time, location, contact information and everything that is in the attached text file.
Nice to have
• It would be nice to see samples where the white logo is used and another where the black one is used.
Should not have
• This is NOT a folded flyer, we will be sticking it on doors and public places. And we will be printing large simple to put on walls. So only one page with few words like an add (the words are in the attached file)

```html
<!DOCTYPE html>
<html lang="en">
<head>
<meta charset="utf-8">
<title>Harvest of Lanterns Conference — MERIVAL 2017</title>
<link rel="stylesheet" href="https://fonts.googleapis.com/css2?family=Montserrat:wght@600;700&family=Oswald:wght@500;600&family=Lato:wght@400;700&display=swap">
<style>
  :root{
    --yellow:#fcd100;
    --yellow-shade:#e3bc00;
    --orange:#e9810c;
    --ink:#1f1f1f;
    --black:#0d0d0d;
    --white:#ffffff;
    --stage:#e4e4e4;
    --muted:#2a2a2a;
  }
  *{margin:0;padding:0;box-sizing:border-box}
  html,body{width:1200px;height:1200px;overflow:hidden;background:var(--stage)}
  .flyer{position:absolute;left:186px;top:20px;width:828px;height:1160px;background:var(--white);overflow:hidden;
    box-shadow:0 4px 18px rgba(0,0,0,.18)}
  .backdrop{position:absolute;left:0;top:540px;width:828px;height:560px;
    background:linear-gradient(180deg,rgba(255,255,255,1) 0%,rgba(228,228,228,.7) 40%,rgba(236,236,236,.8) 75%,rgba(255,255,255,1) 100%)}
  .bands{position:absolute;left:0;top:0}
  .badge{position:absolute;left:0;top:0}
  .badge-name{font-family:"Oswald",sans-serif;font-weight:600;fill:var(--yellow)}
  .headline{position:absolute;left:0;width:828px;text-align:center;font-family:"Montserrat",sans-serif;font-weight:700}
  .headline-top{top:600px;font-size:52px;letter-spacing:2px;color:var(--ink)}
  .headline-box{position:absolute;left:96px;top:670px;width:640px;height:70px;background:var(--black);
    box-shadow:0 4px 6px rgba(0,0,0,.25);
    font-family:"Montserrat",sans-serif;font-weight:600;font-size:44px;letter-spacing:2px;color:var(--yellow);
    text-align:center;line-height:70px}
  .tagline{top:756px;font-size:19px;letter-spacing:1px;color:var(--ink)}
  .speakers{position:absolute;left:0;top:800px;width:828px;height:68px;background:var(--orange);display:flex}
  .speakers-label{width:157px;height:68px;background:var(--yellow);font-family:"Oswald",sans-serif;font-weight:500;
    font-size:27px;color:var(--ink);text-align:center;line-height:68px;letter-spacing:1px}
  .speakers-list{display:grid;grid-template-columns:210px 172px 240px;grid-template-rows:20px 20px;
    padding:16px 0 0 16px;font-family:"Lato",sans-serif;font-weight:700;font-size:13px;color:var(--white);list-style:none}
  .speakers-list li::before{content:"•";margin-right:2px}
  .dates{position:absolute;left:120px;top:898px;width:285px;font-family:"Oswald",sans-serif;font-weight:600;line-height:1;
    white-space:nowrap;transform:scaleX(.8);transform-origin:left top}
  .dates-days{font-size:48px;color:var(--orange);letter-spacing:-1px}
  .dates-month{font-size:48px;color:var(--ink);letter-spacing:-.5px;margin-top:2px}
  .time{position:absolute;left:425px;top:901px;width:310px;height:86px;background:var(--yellow);
    font-family:"Oswald",sans-serif;font-weight:600;font-size:80px;color:var(--ink);text-align:center;line-height:84px}
  .venue{position:absolute;left:40px;top:1036px;display:flex;align-items:center;gap:14px}
  .venue-address{font-family:"Lato",sans-serif;font-size:15px;line-height:17.5px;color:var(--muted);letter-spacing:.3px}
  .hall{position:absolute;left:510px;top:1046px;display:flex;align-items:center;gap:18px;
    font-family:"Lato",sans-serif;font-weight:700;font-size:24px;color:var(--muted);letter-spacing:.6px}
  .contact{position:absolute;left:0;top:1106px;width:828px;height:54px;background:var(--black);display:flex;
    justify-content:center;gap:52px;align-items:center;font-family:"Lato",sans-serif;font-size:18px;color:var(--white);letter-spacing:.5px}
  .contact span{display:flex;align-items:center;gap:7px}
</style>
</head>
<body>
<main class="flyer">
  <div class="backdrop" role="img" aria-label="Faded black-and-white photo of young people gathered in worship"></div>

  <svg class="bands" width="828" height="540" viewBox="0 0 828 540" aria-hidden="true">
    <polygon points="0,168 160,158 160,463 0,463" fill="var(--yellow)"/>
    <polygon points="0,168 55,164 55,463 0,463" fill="var(--yellow-shade)" opacity=".35"/>
    <polygon points="700,158 828,170 828,450 700,463" fill="var(--yellow)"/>
    <polygon points="790,166 828,170 828,450 790,455" fill="var(--yellow-shade)"/>
  </svg>

  <svg class="badge" width="828" height="600" viewBox="0 0 828 600" role="img" aria-label="MERVAL conference badge">
    <circle cx="430" cy="306" r="300" fill="var(--white)"/>
    <circle cx="430" cy="306" r="273" fill="var(--black)"/>
    <circle cx="430" cy="306" r="270" fill="none" stroke="var(--white)" stroke-width="1.5"/>
    <circle cx="430" cy="306" r="260" fill="#222"/>
    <circle cx="430" cy="306" r="255" fill="none" stroke="var(--white)" stroke-width="6" stroke-dasharray="4 5"/>
    <text class="badge-name" x="430" y="205" font-size="84" text-anchor="middle" letter-spacing="4">MERIVAL</text>
    <circle cx="430" cy="290" r="44" fill="none" stroke="var(--yellow)" stroke-width="4"/>
    <text class="badge-name" x="430" y="396" font-size="50" text-anchor="middle" letter-spacing="6">MERVAL</text>
    <text class="badge-name" x="430" y="492" font-size="92" text-anchor="middle">2017</text>
  </svg>

  <h1 class="headline headline-top">HARVEST OF</h1>
  <div class="headline-box">LANTERNS CONFERENCE</div>
  <p class="headline tagline">YOUR SONS AND DAUGHTERS SHALL PROPHESY</p>

  <section class="speakers">
    <div class="speakers-label">SPEAKERS</div>
    <ul class="speakers-list">
      <li>Prophet Lucien Marovi</li>
      <li>Prophet Samuel Okoro</li>
      <li>Prophet Noel Adrien Matesi</li>
      <li>Bishop Aaron Tembeli</li>
      <li>Prophet Jonas Velari</li>
    </ul>
  </section>

  <div class="dates">
    <div class="dates-days">1ST, 2ND AND 3RD</div>
    <div class="dates-month">SEPTEMBER 2017</div>
  </div>
  <div class="time">6:00PM</div>

  <div class="venue">
    <svg width="34" height="44" viewBox="0 0 34 44" aria-hidden="true">
      <ellipse cx="17" cy="38" rx="14" ry="5" fill="none" stroke="var(--black)" stroke-width="3"/>
      <path d="M17 2C9 2 4 8 4 14c0 9 13 22 13 22s13-13 13-22C30 8 25 2 17 2z" fill="var(--orange)"/>
      <circle cx="17" cy="14" r="5" fill="var(--white)"/>
    </svg>
    <p class="venue-address">Harborline Meadow Inn<br>412 Elmwood Avenue Northfield,<br>ME 04999 United States</p>
  </div>

  <div class="hall">
    <svg width="32" height="32" viewBox="0 0 32 32" aria-hidden="true">
      <path d="M16 3 2 15h4v14h20V15h4z" fill="var(--orange)"/>
      <rect x="12" y="18" width="8" height="11" fill="var(--white)"/>
    </svg>
    Cedar Hall Ballroom
  </div>

  <footer class="contact">
    <span><svg width="12" height="12" viewBox="0 0 12 12" aria-hidden="true"><path d="M2 1l2.5 0 1 3-1.5 1a7 7 0 0 0 3 3l1-1.5 3 1V11C6 11 1 6 1 2z" fill="var(--white)"/></svg>+1 (555) 014 2290</span>
    <span><svg width="14" height="11" viewBox="0 0 14 11" aria-hidden="true"><rect x="1" y="1" width="12" height="9" fill="none" stroke="var(--white)" stroke-width="1.5"/><path d="M1 1l6 5 6-5" fill="none" stroke="var(--white)" stroke-width="1.5"/></svg>hello@lanterngrove.org</span>
    <span><svg width="13" height="13" viewBox="0 0 13 13" aria-hidden="true"><circle cx="6.5" cy="6.5" r="5.5" fill="none" stroke="var(--white)" stroke-width="1.5"/><path d="M1 6.5h11M6.5 1c-3 3-3 8 0 11M6.5 1c3 3 3 8 0 11" fill="none" stroke="var(--white)" stroke-width="1.2"/></svg>http://merval-events.org</span>
  </footer>
</main>
</body>
</html>
```